Closing Airway Heights Clinic

We are closing one of our two clinics and want to encourage our patients at Airway Heights clinic to see us at our Spokane Valley Clinic.

Target Market(s)

Our current patients. Male and female, but women make most healthcare choices for family. Large military population in our patient base.

Industry/Entity Type

Health Care

Font styles to use
Serif

Requirements
Must have
• Fernpoint Optical has closed our location within the Airway Heights Dalcrest. We would love to see you for continued care at our Spokane Valley (Hartwell Exit) Dalcrest location.
20486 E Calder Ave, Spokane Valley, WA 99037
Call or Text 509-555-0143
Nice to have
• Can use photos from our web site, fernpointcare.com, or from project three years ago. Include photos of Dr Tobin Marsk, Dr Corinne Vasto and Margolie

```html
<!DOCTYPE html>
<html lang="en">
<head>
<meta charset="utf-8">
<title>Fernpoint Optical – We are Open at Spokane Valley</title>
<link href="https://fonts.googleapis.com/css2?family=Montserrat:ital,wght@0,400;0,500;0,600;0,700;1,400&display=swap" rel="stylesheet">
<style>
  :root {
    --brand-blue: #0ba5d3;
    --brand-navy: #1b2d8f;
    --text-gray: #8e8f92;
    --text-dark: #2b2b2b;
    --frame: #9a9a9a;
    --paper: #ffffff;
    --photo-wall: #5a6068;
    --photo-floor: #7a5a3e;
  }
  * { margin: 0; padding: 0; box-sizing: border-box; }
  html, body {
    width: 1200px; height: 1000px; overflow: hidden;
    background: var(--paper);
    font-family: "Montserrat", Arial, sans-serif;
  }
  .postcard {
    position: absolute; left: 303px; width: 591px; height: 399px;
    border: 1px solid var(--frame); background: var(--paper);
  }
  .postcard--front { top: 90px; }
  .postcard--back { top: 496px; }
  .abs { position: absolute; }

  .brand-name {
    display: flex; align-items: center; gap: 6px;
    font-weight: 700; font-size: 15px; color: var(--brand-navy); white-space: nowrap;
  }
  .brand-name--back { left: 318px; top: 40px; width: 180px; justify-content: center; font-size: 14px; }
  .brand-name__dot { width: 12px; height: 12px; border-radius: 50%; background: var(--brand-blue); flex: none; }

  .headline { left: 30px; top: 136px; color: var(--text-gray); }
  .headline__lead { font-size: 26px; font-weight: 600; line-height: 28px; }
  .headline__open { font-size: 60px; font-weight: 700; color: var(--brand-blue); line-height: 54px; letter-spacing: -1px; }
  .headline__place { font-size: 26px; font-weight: 600; line-height: 34px; }

  .notice {
    left: 295px; top: 112px; width: 292px;
    font-style: italic; font-size: 11px; line-height: 13.4px; color: var(--text-dark);
  }
  .team { left: 295px; top: 175px; width: 290px; }
  .team__member { position: absolute; top: 0; width: 95px; text-align: center; }
  .team__photo {
    display: block; margin: 0 auto; width: 84px; height: 84px; border-radius: 50%;
    border: 1px solid #222;
    background: radial-gradient(circle at 50% 40%, #d9c2b0 0%, #b79a86 35%, #e8e8e8 70%);
  }
  .team__name { margin-top: 3px; font-size: 8.4px; font-weight: 500; color: var(--text-dark); white-space: nowrap; }

  .contact { left: 0; width: 100%; top: 323px; text-align: center; }
  .contact__label { font-size: 19.5px; font-weight: 500; color: var(--text-gray); line-height: 22px; margin-left: -5px; }
  .contact__phone { font-size: 33px; font-weight: 600; color: var(--brand-blue); line-height: 36px; }

  .history { left: 30px; top: 20px; width: 225px; font-size: 10.3px; line-height: 12px; color: var(--text-gray); }
  .clinic-photo {
    left: 30px; top: 87px; width: 224px; height: 224px; border-radius: 50%;
    border: 1px solid #999;
    background: linear-gradient(160deg, #3c4148 0%, var(--photo-wall) 45%, #2a2a2a 70%, var(--photo-floor) 100%);
  }
  .appointment { left: 28px; top: 332px; color: var(--text-gray); }
  .appointment__title { font-size: 21.5px; font-weight: 500; color: var(--brand-blue); line-height: 24px; }
  .appointment__line { font-size: 14.5px; font-weight: 500; line-height: 17px; }

  .divider { left: 296px; top: 21px; width: 1px; height: 365px; background: var(--frame); }
  .stamp-box { left: 506px; top: 21px; width: 68px; height: 68px; border: 1px solid var(--frame); }
  .address-line { left: 318px; width: 256px; height: 1px; background: var(--frame); }
  .website {
    left: 312px; width: 264px; top: 367px; text-align: right; white-space: nowrap;
    font-size: 20.5px; font-weight: 500; color: var(--brand-blue); line-height: 24px;
  }
</style>
</head>
<body>

<section class="postcard postcard--front">
  <div class="abs brand-name" style="right:18px; top:52px;"><span class="brand-name__dot"></span>Fernpoint Optical</div>

  <div class="abs headline">
    <p class="headline__lead">We are</p>
    <p class="headline__open">Open</p>
    <p class="headline__place">at Spokane Valley</p>
  </div>

  <p class="abs notice">“Fernpoint Optical has closed our location within the Airway Heights Dalcrest. We would love to see you for continued care at our Spokane Valley (Hartwell Exit) Dalcrest location”</p>

  <div class="abs team">
    <div class="team__member" style="left:0;">
      <span class="team__photo" role="img" aria-label="Portrait photo of Dr Tobin Marsk"></span>
      <p class="team__name">Dr Tobin Marsk</p>
    </div>
    <div class="team__member" style="left:96px;">
      <span class="team__photo" role="img" aria-label="Portrait photo of Dr Corinne Vasto"></span>
      <p class="team__name">Dr Corinne Vasto</p>
    </div>
    <div class="team__member" style="left:191px;">
      <span class="team__photo" role="img" aria-label="Portrait photo of Manager Margolie"></span>
      <p class="team__name">Manager, Margolie</p>
    </div>
  </div>

  <div class="abs contact">
    <p class="contact__label">Call or Text</p>
    <p class="contact__phone">509-555-0143</p>
  </div>
</section>

<section class="postcard postcard--back">
  <p class="abs history">Dr. Marsk and his friendly team of eyecare specialists have been helping Spokane see better since 2000!</p>

  <div class="abs clinic-photo" role="img" aria-label="Photo of the clinic reception desk and waiting area"></div>

  <div class="abs appointment">
    <p class="appointment__title">Make an Appointment</p>
    <p class="appointment__line">20486 E Calder Ave,</p>
    <p class="appointment__line">Spokane Valley, WA 99037</p>
  </div>

  <div class="abs divider"></div>

  <div class="abs brand-name brand-name--back"><span class="brand-name__dot"></span>Fernpoint Optical</div>
  <div class="abs stamp-box"></div>

  <div class="abs address-line" style="top:151px;"></div>
  <div class="abs address-line" style="top:183px;"></div>
  <div class="abs address-line" style="top:215px;"></div>
  <div class="abs address-line" style="top:246px;"></div>

  <p class="abs website">www.fernpointcare.com</p>
</section>

</body>
</html>
```